Wordpress Design Project - IT Consulting Services Web Site

Our are starting a new technology services company. We will provide services in software implementation and business intelligence.

We need a beautiful Wordpress web site design. We need a design for the homepage, and one interior content page.

The site must have a very professional and polished look and feel. What I have suggested below are things that I think work, but I am not a designer and I am open to your professional opinions. Please be willing to use your best judgment.

The homepage should have the following elements:
- A Header Area that includes:
o The company logo, and
o navigation (consistent with the interior page)
o a social media link section that includes rss feeds, youtube, facebook, linkedin and tweets
- A Body that includes:
o A slider
o An area that features up to six of the most recent or important posts including a thumbnail and small picture, a title, and a short excerpt for each.
o An area for around 100 words of text and an image
- A footer that includes:
o The company logo
o Contact information

The interior page is relatively simple. It should include the same navigation element as the homepage, and accommodate a one column text layout.

The current site …
You can visit the current site at www.korvelpath.com I built the current site using the “Velthor Quick Pane” premium theme. If you visit this site you get a sense of some of the things I am talking about, but there are things that I do not like about the current site. Here’s what I like and what I don’t like.

What I like about the current site:
- It is reactive – it adapts to the size of the viewing browser
- It has a “metro” feel to it. The company will have an association with Microsoft and having a “metro” theme is a plus, but not a requirement.
- It is different without being hard to navigate – the site the slider is from the “glide cascade widget”, the posts are represented with tiles and rearrange themselves when a topic is selected.

What I don’t like:
- The site lacks a cohesive feel – it feels to me like a bunch of different elements without a single theme that pulls everything together.
- It is not aesthetically appealing to me.
- The tiles in the post section are too big.
- I don’t like the white background – I would prefer a background color and ideally a background that somehow incorporates the graphic in the logo.

About themes
As I said, I used a Velthor theme in my design. I will be happy to continue using this theme, or would be willing to buy a new premium theme, so long as the cost is less than $100 U.S.

Site Map:
What we do
ERP Implementation
Business Intelligence
Who we are
What’s different about us
Principles
Mission, Vision, Values
Actions
How we work
What’s Different About Us
Blogs
What Papers
Presentations
Join
What we are looking for
What are you looking for?
Benefits
Context
Updates

Regarding Pictures
Please do not feel you need to use any of the pictures currently on the site.  Use whatever pictures you feel look best.  Comps are okay. 

It is not necessary to use any of the content on the current site - you do not need to use either the pictures or the text.  Please feel free to use pictures of your choice (comps okay), and/or lorem text.

The top level navigation is the navigation I would like.

Hello all,

Since this is a Wordpress project, it goes without saying I will need to implement this design in Wordpress.  It is not absolutely necessary that a design that matches an existing template (free or not), but a design that does will have an advantage over a design which requires that a new template be coded from scratch.

Thank you.

Target Market(s)

Business executives and potential employees

Industry/Entity Type

Software

Requirements
Nice to have
• It would be nice if the site was reactive.

```html
<!DOCTYPE html>
<html lang="en">
<head>
<meta charset="utf-8">
<title>KorvelPath – Home</title>
<link href="https://fonts.googleapis.com/css2?family=Ubuntu:ital,wght@0,300;0,400;0,500;0,700;1,500;1,700&display=swap" rel="stylesheet">
<style>
:root{
  --page-bg:#f2f2ef;
  --card-border:#d6d6d6;
  --title-blue:#1b86d0;
  --accent-orange:#d08a00;
  --body-text:#5a5a5a;
  --rule-grey:#c9c9c9;
  --event-blue:#1a76b9;
  --event-line:#4d97cd;
  --yellow-top:#ffe58a;
  --yellow-bottom:#f5b81c;
  --dark-box:#1d1b19;
  --input-grey:#4a4a4a;
  --tan:#d9a55a;
  --footer-top:#2f90c9;
  --footer-bottom:#0b69a5;
  --white:#ffffff;
}
*{margin:0;padding:0;box-sizing:border-box}
html,body{width:1137px;height:1200px;overflow:hidden}
body{position:relative;background:var(--page-bg);font-family:'Ubuntu',sans-serif;color:var(--body-text)}
.abs{position:absolute}

/* posts */
.post-thumb{position:absolute;width:294px;height:176px;background:var(--white);border:1px solid var(--card-border);padding:5px}
.post-thumb .photo{width:100%;height:100%}
.photo-road{background:linear-gradient(180deg,#6f9a4a 0%,#3f6a2c 45%,#8a8a7a 75%,#5c5d52 100%)}
.photo-car{background:linear-gradient(180deg,#a9b6c0 0%,#8f8a73 35%,#2f3a3a 65%,#6a6b66 100%)}
.post-title{position:absolute;font-size:16px;font-weight:500;color:var(--title-blue);white-space:nowrap}
.post-date{position:absolute;font-size:11px;font-weight:700;font-style:italic;color:var(--accent-orange);text-transform:uppercase}
.post-excerpt{position:absolute;width:290px;font-size:13.5px;line-height:19px;color:var(--body-text)}
.read-more{position:absolute;font-size:13px;font-weight:700;font-style:italic;color:var(--accent-orange)}
.read-more span{font-style:normal;margin-left:6px;font-weight:400}
.post-rule{position:absolute;width:296px;height:5px;background:repeating-linear-gradient(135deg,#bdbdbd 0 2px,#dedede 2px 4px)}

/* sidebar */
.side-frame{position:absolute;left:760px;width:318px;background:var(--white);border:1px solid #e2e2e2}
.events{position:absolute;left:765px;top:48px;width:307px;height:421px;background:var(--event-blue);color:var(--white)}
.events h2{position:absolute;left:15px;top:10px;font-size:23px;font-weight:500}
.events .line{position:absolute;left:0;width:100%;height:1px;background:var(--event-line)}
.events .day{position:absolute;left:18px;font-size:16px;font-weight:700;font-style:italic}
.events .slot{position:absolute;left:18px;width:270px;font-size:13.5px;line-height:18px}
.events .slot b{font-weight:700}
.btn-yellow{position:absolute;left:775px;width:289px;background:linear-gradient(180deg,var(--yellow-top),var(--yellow-bottom));border:1px solid #e0a615}
.btn-yellow .label{position:absolute;left:56px;top:12px;font-size:22px;font-weight:700;color:#2a2212}
.newsletter{position:absolute;left:765px;top:498px;width:307px;height:95px;background:var(--dark-box)}
.newsletter h3{position:absolute;left:15px;top:9px;font-size:25px;font-weight:300;color:var(--white)}
.newsletter .field{position:absolute;left:16px;top:47px;width:185px;height:31px;background:var(--input-grey);color:#e6e6e6;font-size:13.5px;padding:7px 8px}
.newsletter .submit{position:absolute;left:201px;top:47px;width:98px;height:31px;background:var(--tan);color:#1d1b19;font-size:14.5px;font-weight:700;text-align:center;padding-top:7px}

/* footer */
.site-footer{position:absolute;left:0;top:778px;width:1137px;height:422px;background:linear-gradient(180deg,var(--footer-top),var(--footer-bottom));border-top:4px solid #cfd3d6;color:var(--white)}
.foot-col{position:absolute;top:36px}
.foot-col h4{font-size:14.5px;font-weight:700;font-style:italic;text-transform:uppercase;padding-bottom:8px;border-bottom:2px solid var(--white);width:184px}
.foot-col ul{list-style:none;margin-top:12px;padding-left:4px}
.foot-col li{font-size:13.5px;line-height:25.3px}
.contact p{font-size:13.5px;line-height:25.3px;padding-left:4px;margin-top:12px}
.contact p span{display:block}
.brand{position:absolute;left:648px;top:210px;font-size:40px;font-weight:400;color:#d5ecfa;letter-spacing:-0.5px}
.brand-dot{position:absolute;left:958px;top:160px;width:46px;height:46px;border-radius:50%;background:#4fb8ea}
.foot-rule{position:absolute;left:68px;top:346px;width:990px;height:2px;background:var(--white)}
.copyright{position:absolute;left:0;top:378px;width:1137px;text-align:center;font-size:13.5px}
</style>
</head>
<body>

<!-- posts -->
<div class="post-thumb" style="left:59px;top:7px"><div class="photo photo-road" role="img" aria-label="Vintage convertible driving down a tree-lined country road"></div></div>
<div class="post-title" style="left:61px;top:199px">LOREM IPSUM DOLOR SIT AMET</div>
<div class="post-date" style="left:61px;top:219px">Posted on March 7th, 2012.</div>
<div class="post-excerpt" style="left:61px;top:243px">Many also have no hope of paying the mortgage, feeding the kids, or buying gas to fuel the car to get to a job interview.</div>
<div class="read-more" style="left:61px;top:310px">Read More<span>»</span></div>
<div class="post-rule" style="left:59px;top:344px"></div>

<div class="post-thumb" style="left:408px;top:7px"><div class="photo photo-car" role="img" aria-label="Classic open roadster in a village street"></div></div>
<div class="post-title" style="left:410px;top:199px">LOREM IPSUM DOLOR SIT AMET</div>
<div class="post-date" style="left:410px;top:219px">Posted on March 7th, 2012.</div>
<div class="post-excerpt" style="left:410px;top:243px">Many also have no hope of paying the mortgage, feeding the kids, or buying gas to fuel the car to get to a job interview.</div>
<div class="read-more" style="left:410px;top:310px">Read More<span>»</span></div>
<div class="post-rule" style="left:408px;top:344px"></div>

<div class="post-thumb" style="left:59px;top:385px"><div class="photo photo-road" role="img" aria-label="Vintage convertible driving down a tree-lined country road"></div></div>
<div class="post-title" style="left:61px;top:576px">LOREM IPSUM DOLOR SIT AMET</div>
<div class="post-date" style="left:61px;top:596px">Posted on March 7th, 2012.</div>
<div class="post-excerpt" style="left:61px;top:620px">Many also have no hope of paying the mortgage, feeding the kids, or buying gas to fuel the car to get to a job interview.</div>
<div class="read-more" style="left:61px;top:687px">Read More<span>»</span></div>
<div class="post-rule" style="left:59px;top:721px"></div>

<div class="post-thumb" style="left:408px;top:385px"><div class="photo photo-car" role="img" aria-label="Classic open roadster in a village street"></div></div>
<div class="post-title" style="left:410px;top:576px">LOREM IPSUM DOLOR SIT AMET</div>
<div class="post-date" style="left:410px;top:596px">Posted on March 7th, 2012.</div>
<div class="post-excerpt" style="left:410px;top:620px">Many also have no hope of paying the mortgage, feeding the kids, or buying gas to fuel the car to get to a job interview.</div>
<div class="read-more" style="left:410px;top:687px">Read More<span>»</span></div>
<div class="post-rule" style="left:408px;top:721px"></div>

<!-- sidebar -->
<div class="side-frame" style="top:-2px;height:22px"></div>
<div class="btn-yellow" style="top:-2px;height:12px"></div>

<div class="side-frame" style="top:43px;height:430px"></div>
<div class="events">
  <h2>LATEST EVENTS</h2>
  <div class="line" style="top:50px"></div>
  <div class="day" style="top:61px">Thursday 19 September 2010</div>
  <div class="slot" style="top:91px"><b>18.00 – 19.30</b>&nbsp; Welcome Cocktail</div>
  <div class="slot" style="top:116px"><b>19.30+</b>&nbsp;&nbsp;&nbsp;&nbsp;&nbsp;&nbsp;&nbsp;&nbsp;&nbsp;&nbsp; Free evening program</div>
  <div class="day" style="top:153px">Friday&nbsp; 20 September 2010</div>
  <div class="slot" style="top:186px"><b>08.30 – 12.30</b>&nbsp; Stage 1: Lugano - &nbsp;Lago Maggiore</div>
  <div class="slot" style="top:229px"><b>12.30 – 14.30</b>&nbsp; Lunch</div>
  <div class="slot" style="top:255px"><b>14.30 – 17.30</b>&nbsp; Stage 2: Lago Maggiore - Lugano</div>
  <div class="slot" style="top:298px"><b>19.30 – 22.00</b>&nbsp; Dinner &nbsp;&amp; Wine Tasting</div>
  <div class="line" style="top:350px"></div>
</div>
<div class="btn-yellow" style="top:409px;height:51px">
  <div class="label">MORE EVENTS</div>
  <svg class="abs" style="left:229px;top:19px" width="32" height="14" viewBox="0 0 32 14" aria-hidden="true">
    <g fill="#2a2212"><path d="M0 0h4l6 7-6 7H0l6-7z"/><path d="M11 0h4l6 7-6 7h-4l6-7z"/><path d="M22 0h4l6 7-6 7h-4l6-7z"/></g>
  </svg>
</div>

<div class="side-frame" style="top:493px;height:105px"></div>
<div class="newsletter">
  <h3>Subscribe Newsletter</h3>
  <div class="field">Type your email id here</div>
  <div class="submit">SUBSCRIBE</div>
</div>

<!-- footer -->
<footer class="site-footer">
  <div class="foot-col" style="left:68px">
    <h4>Qucik Links 1</h4>
    <ul>
      <li>What we do</li><li>ERP Implementation</li><li>Business Intelligence</li><li>Who we are</li>
      <li>What’s different about us</li><li>Principles</li><li>Mission, Vision, Values</li><li>Actions</li>
    </ul>
  </div>
  <div class="foot-col" style="left:351px">
    <h4>Qucik Links 2</h4>
    <ul>
      <li>How we work</li><li>What’s Different About Us</li><li>Blogs</li><li>What Papers</li>
      <li>Presentations</li><li>Join</li><li>What we are looking for</li><li>What are you looking for?</li>
    </ul>
  </div>
  <div class="foot-col contact" style="left:631px">
    <h4>Contact Information</h4>
    <p>
      <span>48/2 Harlow Avenue, Suite No 310, 2nd Floor,</span>
      <span>Block C &amp; D, Fenwick, Springfield, USA,</span>
      <span>Phone : 555 0142 7788, Email id: info@korvelpath.com</span>
    </p>
  </div>
  <div class="brand-dot"></div>
  <div class="brand">KorvelPath</div>
  <div class="foot-rule"></div>
  <div class="copyright">© 2013, All Rights Reserved, korvelpath.com</div>
</footer>

</body>
</html>
```